Website banners + icons

Hello,

For our website www.morvelquintas.com who is a very serious website for immigration, integration and naturalisation in Switzerland, we need :

3 x homepage banners : 998px/300px
10 x banners : 998px/150px (concerns the website pages)
icons 24px/24px

The idea is to present a black/white banners with the current text and the theme must be in accordance with the page title.

The graphic line must be very clean and including some fine red informations or line or what ever but very clean and design full.

Please do not use stereotypes like hand shakes...

We are also open to work with abstract things or art.

We let your creativity works on.

Good luck

```html
<!DOCTYPE html>
<html lang="en">
<head>
<meta charset="utf-8">
<title>Morvel Quintas – Home</title>
<link rel="stylesheet" href="https://fonts.googleapis.com/css2?family=Arimo:wght@400;700&display=swap">
<style>
  :root {
    --backdrop: #2b2b2b;
    --backdrop-edge: #1c1c1c;
    --page: #ffffff;
    --ink: #1b1b1b;
    --muted: #6e6e6e;
    --soft: #8a8a8a;
    --accent: #e30613;
    --hero-light: #a8a8a8;
    --hero-dark: #5a5a5a;
    --caption-bg: rgba(20, 20, 20, 0.88);
  }
  * { box-sizing: border-box; margin: 0; padding: 0; }
  html, body { width: 1200px; height: 770px; overflow: hidden; }
  body {
    font-family: "Arimo", Arial, sans-serif;
    background: radial-gradient(ellipse at center, var(--backdrop) 0%, var(--backdrop-edge) 100%);
    position: relative;
  }
  .page {
    position: absolute;
    left: 172px; top: 3px;
    width: 877px; height: 767px;
    background: var(--page);
    overflow: hidden;
  }
  .site-header { position: relative; height: 202px; }
  .brand {
    position: absolute; left: 21px; top: 74px;
    display: flex; align-items: center; gap: 10px;
    font-size: 27px; font-weight: 400; letter-spacing: 1px;
    color: var(--ink); text-transform: uppercase;
  }
  .brand-mark { width: 14px; height: 14px; background: var(--ink); }
  .language {
    position: absolute; left: 731px; top: 34px; width: 120px;
    display: flex; align-items: center; gap: 8px;
    font-size: 11px; color: var(--ink);
  }
  .language .caret {
    margin-left: auto;
    width: 0; height: 0;
    border-left: 4px solid transparent; border-right: 4px solid transparent;
    border-top: 4px solid #b5b5b5;
  }
  .main-nav {
    position: absolute; left: 21px; top: 159px;
    display: flex; list-style: none;
    font-size: 11px; letter-spacing: 0.6px; color: var(--muted);
  }
  .main-nav li { padding: 0 15px; border-left: 1px solid #d6d6d6; line-height: 18px; }
  .main-nav li:first-child { padding-left: 0; border-left: none; }
  .main-nav li.current { color: var(--accent); }
  .hero {
    position: relative; height: 355px;
    background: linear-gradient(110deg, var(--hero-light) 0%, #8c8c8c 50%, var(--hero-dark) 100%);
  }
  .hero-caption {
    position: absolute; left: 431px; top: 201px;
    width: 417px; height: 136px;
    background: var(--caption-bg);
    padding: 10px 0 0 26px;
  }
  .hero-title { font-size: 58px; font-weight: 400; color: #fff; line-height: 64px; letter-spacing: 0.5px; }
  .hero-tagline { margin-top: 8px; font-size: 21px; color: var(--accent); line-height: 26px; }
  .section-head {
    position: absolute; left: 22px; top: 596px; right: 22px;
    display: flex; align-items: center; gap: 10px;
  }
  .section-head h1 { font-size: 17px; font-weight: 400; letter-spacing: 1.5px; color: var(--muted); }
  .section-head .dots { flex: 1; border-top: 2px dotted #d3d3d3; height: 0; }
  .features { position: absolute; left: 21px; top: 652px; width: 860px; }
  .feature { position: absolute; top: 0; width: 210px; }
  .feature svg { position: absolute; left: 0; top: 0; }
  .feature h2 {
    position: absolute; left: 39px; top: 3px;
    font-size: 15px; font-weight: 400; color: var(--muted); white-space: nowrap;
  }
  .feature p {
    position: absolute; left: 39px; top: 39px; width: 170px;
    font-size: 11px; line-height: 16px; color: var(--soft); white-space: nowrap;
  }
</style>
</head>
<body>
  <div class="page">
    <header class="site-header">
      <div class="brand"><span class="brand-mark"></span>Morvel Quintas</div>
      <div class="language">
        <svg width="16" height="10" viewBox="0 0 16 10" aria-hidden="true">
          <rect width="16" height="10" fill="#1f3a8a"/>
          <path d="M0 0L16 10M16 0L0 10" stroke="#fff" stroke-width="2"/>
          <rect x="6.5" width="3" height="10" fill="#fff"/>
          <rect y="3.5" width="16" height="3" fill="#fff"/>
          <rect x="7.2" width="1.6" height="10" fill="#c8102e"/>
          <rect y="4.2" width="16" height="1.6" fill="#c8102e"/>
        </svg>
        <span>English</span>
        <span class="caret"></span>
      </div>
      <ul class="main-nav">
        <li class="current">Home</li>
        <li>Services</li>
        <li>Clients</li>
        <li>Blog</li>
        <li>Contact</li>
        <li>About Us</li>
      </ul>
    </header>

    <section class="hero" role="img" aria-label="Black and white close-up photograph of watch movement gears">
      <div class="hero-caption">
        <div class="hero-title">Integration</div>
        <div class="hero-tagline">Local regulation<br>Guidance</div>
      </div>
    </section>

    <div class="section-head"><h1>HOME</h1><span class="dots"></span></div>

    <div class="features">
      <article class="feature" style="left:0">
        <svg width="22" height="22" viewBox="0 0 22 22" aria-hidden="true" fill="var(--accent)">
          <rect x="0" y="16" width="3" height="5"/><rect x="5" y="12" width="3" height="9"/>
          <rect x="10" y="8" width="3" height="13"/><rect x="15" y="4" width="3" height="17"/>
          <rect x="19.5" y="0" width="2.5" height="21"/>
        </svg>
        <h2>Immigration</h2>
        <p>Moving to a new country with<br>different rules and regulations<br>is a big step. Living costs,<br>admini- strative hurdles as<br>well as every day life will be</p>
      </article>
      <article class="feature" style="left:216px">
        <svg width="22" height="22" viewBox="0 0 22 22" aria-hidden="true" fill="none" stroke="var(--accent)" stroke-width="3" stroke-linecap="round">
          <path d="M4 18L15 7"/><circle cx="16.5" cy="5.5" r="3.5" stroke-width="2.5"/>
          <path d="M4 4L18 18"/><path d="M2 2L5 5" stroke-width="4"/>
        </svg>
        <h2>Integration</h2>
        <p>After having decided to make<br>Switzerland your home, the<br>conditions of residency will<br>change. Morvel Quintas offers<br>professional support and</p>
      </article>
      <article class="feature" style="left:433px">
        <svg width="32" height="32" viewBox="0 0 32 32" aria-hidden="true">
          <rect width="32" height="32" fill="var(--accent)"/>
          <rect x="13" y="6" width="6" height="20" fill="#fff"/>
          <rect x="6" y="13" width="20" height="6" fill="#fff"/>
        </svg>
        <h2>Naturalization</h2>
        <p>After making Switzerland<br>home, the next step to be<br>considered is obtaining<br>Swiss citizenship.<br>Morvel Quintas experts safely</p>
      </article>
      <article class="feature" style="left:650px">
        <svg width="32" height="22" viewBox="0 0 32 22" aria-hidden="true" fill="var(--accent)">
          <ellipse cx="11" cy="8" rx="10" ry="7"/><path d="M4 13L2 19L9 14Z"/>
          <ellipse cx="21" cy="12" rx="9" ry="6.5" stroke="#fff" stroke-width="1.5"/><path d="M26 16L29 21L22 17Z"/>
        </svg>
        <h2>Legal advice</h2>
        <p>Living in a country with a<br>different legal system is a<br>challenge in itself.<br>Morvel Quintas experts are<br>specialized in contract as</p>
      </article>
    </div>
  </div>
</body>
</html>
```